TV - business card

Tidewell Vantage is an insurance brokerage firm, inovative, proactive, vigorous, which aims to become the leader of the insurance brokers in Anfrica. We should like to get some designs which should be avoided also in Gray / Metallic for the Administration and Orange / Blue for the Managers (ike in the picture sent). The Blue / Green logo is not the correct one, but the source of the file. Please adjust the color accordingly for the business cards. 1 / Orange / Blue 2 / Gray / Metallic We want something classic but which is transmitted strenght, inovation, modernity and most of all, rapidity. We want something start-up like, very punchy and catching eye remaining profesional at the same time. Name: Delton Ashgrove Function: Managing Director Address: N ° 73/74 Cmt. Bolembe - R / C 2B Esquerda - Bairro Quimbuta - Luanda Tel: (+244) 947 385 619 Email: delton.ashgrove@tidewell-v.com Website: www.tidewell-v. com We want classic in the front and creative, colorfull at the back. The cards will be printed in relief, with very high quality of paper.
Industry/Entity Type
Insurance Broker
Colors
Designer to choose colors to be used in the design.
Look and feel

```html
<!DOCTYPE html>
<html lang="en">
<head>
<meta charset="utf-8">
<title>Tidewell Vantage – Business Card</title>
<link href="https://fonts.googleapis.com/css2?family=Lato:wght@300;400;700&display=swap" rel="stylesheet">
<style>
  :root {
    --stage: #2b2725;
    --card: #0e0e0e;
    --card-edge: #1a1a1a;
    --silver: #8c8c8c;
    --silver-light: #b5b5b5;
    --text-light: #e6e6e6;
    --text-muted: #8a8a8a;
    --rule: #242424;
    --pattern-a: #1a1a1a;
    --pattern-b: #0b0b0b;
    --pattern-c: #040404;
  }
  * { margin: 0; padding: 0; box-sizing: border-box; }
  html, body {
    width: 1200px; height: 844px; overflow: hidden;
    background: var(--stage);
    font-family: "Lato", sans-serif;
  }
  .stage {
    width: 1200px; height: 844px;
    display: flex; align-items: center; justify-content: center; gap: 50px;
  }
  .card {
    position: relative;
    width: 540px; height: 310px;
    background: var(--card);
    border: 1px solid var(--card-edge);
    box-shadow: 0 14px 30px rgba(0,0,0,.45);
    overflow: hidden;
  }
  /* Front */
  .brand {
    position: absolute; left: 170px; width: 320px; top: 26px;
    display: flex; flex-direction: column; align-items: center; gap: 10px;
  }
  .brand-mark {
    width: 70px; height: 70px; border-radius: 50%;
    background: var(--silver);
  }
  .brand-name {
    font-weight: 700; font-size: 24px; line-height: 30px; letter-spacing: .5px;
    color: var(--silver); text-transform: uppercase; white-space: nowrap;
  }
  .divider {
    position: absolute; left: 0; right: 0; top: 152px;
    height: 1px; background: var(--rule);
  }
  .address {
    position: absolute; right: 32px; top: 166px;
    text-align: right; font-style: normal;
    font-weight: 300; font-size: 13px; line-height: 19px;
    color: var(--text-muted);
  }
  .person {
    position: absolute; left: 30px; top: 182px;
  }
  .person-name {
    font-weight: 400; font-size: 20px; line-height: 24px; letter-spacing: .5px;
    color: var(--text-light); text-transform: uppercase;
  }
  .person-role {
    font-weight: 300; font-size: 13px; line-height: 18px;
    color: var(--text-muted); margin-bottom: 12px;
  }
  .contact {
    display: flex; align-items: center; gap: 8px;
    font-weight: 300; font-size: 14px; color: var(--silver-light); line-height: 22px;
  }
  .contact svg { width: 14px; height: 14px; fill: var(--silver-light); flex: none; }
  /* Back */
  .back-pattern {
    position: absolute; inset: 0;
    background:
      radial-gradient(ellipse at 30% 20%, var(--pattern-a), transparent 65%),
      linear-gradient(160deg, var(--pattern-b), var(--pattern-c));
  }
  .back-mark {
    position: absolute; left: 340px; top: 92px;
    width: 26px; height: 26px; border-radius: 50%;
    background: var(--silver-light);
  }
</style>
</head>
<body>
<main class="stage">
  <section class="card card-front">
    <div class="brand">
      <div class="brand-mark"></div>
      <div class="brand-name">Tidewell Vantage</div>
    </div>
    <div class="divider"></div>
    <address class="address">
      N ° 73/74 Cmt. Bolembe - R / C<br>
      2B Esquerda<br>
      Bairro Quimbuta - Luanda
    </address>
    <div class="person">
      <h1 class="person-name">Delton Ashgrove</h1>
      <p class="person-role">Managing Director</p>
      <p class="contact">
        <svg viewBox="0 0 16 16"><path d="M3.5 1.5l2.3 2.8-1.3 1.6c.9 2 2.6 3.7 4.6 4.6l1.6-1.3 2.8 2.3-1.2 2.3C7.5 13.4 2.6 8.5 1.2 2.7z"/></svg>
        (+244) 947 385 619
      </p>
      <p class="contact">
        <svg viewBox="0 0 16 16"><path d="M1 3h14v10H1z M2 4.2v.4l6 4 6-4v-.4z" fill-rule="evenodd"/></svg>
        delton.ashgrove@tidewell-v.com
      </p>
    </div>
  </section>

  <section class="card card-back">
    <div class="back-pattern" role="img" aria-label="Tone-on-tone repeating pattern of the brand symbol in embossed black"></div>
    <div class="back-mark"></div>
  </section>
</main>
</body>
</html>
```